Now Leasing Banner

Looking for a banner that says the following information approx 4' x 30'

Now Leasing Maplewood Terrace 925-318-6054

Target Market(s)

Drive by traffic

Industry/Entity Type

Residential property management

Requirements
Must have
• Clear and readable from a distance

```html
<!DOCTYPE html>
<html lang="en">
<head>
<meta charset="utf-8">
<title>Now Leasing Banner – Maplewood Terrace</title>
<link rel="stylesheet" href="https://fonts.googleapis.com/css2?family=Roboto+Condensed:wght@900&family=Figtree:wght@400&display=swap">
<style>
  :root {
    --canvas: #000000;
    --banner-yellow: #FFF200;
    --banner-red: #ED1C24;
    --shadow-red: #8E1518;
    --ink: #000000;
    --paper: #FFFFFF;
  }
  html, body {
    margin: 0;
    padding: 0;
    width: 1200px;
    height: 1000px;
    overflow: hidden;
    background: var(--canvas);
  }
  .artboard {
    position: relative;
    width: 1200px;
    height: 1000px;
    background: var(--canvas);
  }
  .size-note {
    position: absolute;
    left: 68px;
    top: 380px;
    margin: 0;
    font-family: "Figtree", Arial, sans-serif;
    font-weight: 400;
    font-size: 23px;
    line-height: 1;
    color: var(--paper);
  }
  .banner {
    position: absolute;
    left: 63px;
    top: 416px;
    width: 1073px;
    height: 143px;
    display: block;
  }
  .banner-text {
    font-family: "Roboto Condensed", "Arial Narrow", sans-serif;
    font-weight: 900;
  }
  .now-badge { fill: var(--paper); }
  .now-shadow { fill: var(--shadow-red); }
  .headline {
    fill: var(--ink);
    stroke: var(--banner-yellow);
    stroke-width: 6px;
    stroke-linejoin: round;
    paint-order: stroke;
  }
  .phone { fill: var(--banner-red); }
</style>
</head>
<body>
  <main class="artboard">
    <p class="size-note">Size 30X4 Feet</p>

    <svg class="banner" viewBox="0 0 1073 143" role="img" aria-label="Now leasing Maplewood Terrace, call 925-318-6054">
      <rect class="banner-field" x="0" y="0" width="1073" height="143" fill="var(--banner-yellow)"/>
      <polygon class="banner-corner" points="0,0 309,0 90,143 0,143" fill="var(--banner-red)"/>

      <g class="banner-text" transform="translate(96 69) rotate(-33)">
        <text class="now-shadow" x="4" y="30" font-size="74" text-anchor="middle" textLength="180" lengthAdjust="spacingAndGlyphs">NOW</text>
        <text class="now-badge" x="0" y="26" font-size="74" text-anchor="middle" textLength="180" lengthAdjust="spacingAndGlyphs">NOW</text>
      </g>

      <text class="banner-text headline" x="192" y="80" font-size="79" textLength="857" lengthAdjust="spacingAndGlyphs">LEASING MAPLEWOOD TERRACE</text>

      <text class="banner-text phone" x="452" y="132" font-size="56" textLength="334" lengthAdjust="spacingAndGlyphs">925-318-6054</text>
    </svg>
  </main>
</body>
</html>
```